Website Redesign for an Appointment Setting and Lead Generation Company.

I need to redesign an existing website. The website that we are looking to be redesigned is www.trellisvane.example. TrellisVane is a B2B appointment setting organization. The idea is to present a modern look website for professional services company. The idea is to engage the user, look at various services and generate more inbound leads for the website

Target Market(s)

US, APAC, Europe, UK. Focused on B2B companies more than $100 Mn

Industry/Entity Type

Professional Service

Number of Pages Required

5+ page

Font styles to use
Other font styles liked:
• Roboto

Requirements
Must have
• Home Page - Banner Image, Section for Client testimonials
Industry Page - To show industry capabilities
Services Page - To show service capabilities
Blogs Page - to show blogs
Offerings Page - Offerings Page
Nice to have
• I would like to have a elegant design with small animation. Preferably use colors from the logo attached. Use infographics where possible

```html
<!DOCTYPE html>
<html lang="en">
<head>
<meta charset="utf-8">
<title>TrellisVane – Power Your Pipeline</title>
<link href="https://fonts.googleapis.com/css2?family=Roboto:ital,wght@0,400;0,500;0,700;0,900;1,400&display=swap" rel="stylesheet">
<style>
:root{
  --brand-red:#d0393b;
  --ink:#2b2b2b;
  --text-grey:#7a7a7a;
  --hero-sand:#efe6d3;
  --hero-sand-deep:#e6d9bd;
  --footer-bg:#4a4a4c;
  --footer-line:#6a6a6c;
  --white:#ffffff;
}
*{margin:0;padding:0;box-sizing:border-box}
html,body{width:881px;height:1200px;overflow:hidden;background:var(--white)}
body{font-family:'Roboto',sans-serif;color:var(--ink);position:relative}

/* Header */
.site-header{position:absolute;left:0;top:0;width:881px;height:71px;background:var(--white)}
.brand{position:absolute;left:82px;top:13px;display:flex;flex-direction:column}
.brand-row{display:flex;align-items:center;gap:7px}
.brand-dot{width:30px;height:30px;border-radius:50%;background:var(--brand-red)}
.brand-name{font-size:29px;font-weight:700;color:var(--brand-red);line-height:1}
.brand-tagline{font-size:12px;color:var(--ink);margin-left:95px;margin-top:3px}
.main-nav{position:absolute;left:337px;top:28px;display:flex;gap:19px;font-size:12.6px;font-weight:500}
.main-nav a{color:var(--ink);text-decoration:none}
.main-nav a.active{color:var(--brand-red)}
.contact-btn{position:absolute;left:706px;top:17px;width:93px;height:38px;border:1.5px solid var(--brand-red);border-radius:19px;color:var(--brand-red);font-size:12.6px;font-weight:500;display:flex;align-items:center;justify-content:center}

/* Hero */
.hero-bg{position:absolute;left:0;top:71px}
.hero-title{position:absolute;left:85px;top:130px;font-size:58px;font-weight:700;line-height:63px;color:var(--ink);letter-spacing:-1.2px}
.hero-cta{position:absolute;left:85px;top:330px;width:205px;height:45px;border-radius:23px;background:var(--brand-red);color:var(--white);font-size:13px;font-weight:700;display:flex;align-items:center;justify-content:center}
.hero-illustration{position:absolute;left:352px;top:76px;width:510px;height:420px;border-radius:40px;background:radial-gradient(ellipse at 55% 50%,#f4f1e6 0%,#e9efe4 35%,rgba(239,230,211,0) 72%)}

/* Testimonials */
.section-title{position:absolute;left:81px;top:587px;font-size:37px;font-weight:900;line-height:46px;color:var(--ink);letter-spacing:-0.6px}
.client-photo{position:absolute;left:83px;top:711px;width:153px;height:146px;border-radius:50%;background:linear-gradient(135deg,#c9cfd2,#e3d2c4 55%,#8a8c8f);border:8px solid #6b6b6d}
.quote{position:absolute;left:274px;top:710px;width:452px;font-size:13.2px;font-style:italic;line-height:24.6px;color:var(--text-grey)}
.client-role{position:absolute;left:274px;top:825px;font-size:14px;font-weight:500;color:#3a3a3a}
.client-company{position:absolute;left:274px;top:848px;font-size:12.3px;color:#555}
.slider-btn{position:absolute;top:883px;width:37px;height:37px;border-radius:50%;background:var(--white);box-shadow:0 1px 5px rgba(0,0,0,.15);display:flex;align-items:center;justify-content:center}

/* Footer */
.site-footer{position:absolute;left:0;top:961px;width:881px;height:239px;background:var(--footer-bg);color:var(--white)}
.footer-brand{position:absolute;left:82px;top:54px}
.footer-brand .brand-row{gap:9px}
.footer-brand .brand-dot{width:34px;height:34px;background:var(--white)}
.footer-brand .brand-name{font-size:37px;color:var(--white)}
.footer-brand .brand-tagline{color:var(--white);font-size:15px;margin-left:122px;margin-top:4px}
.footer-col{position:absolute;top:28px}
.footer-col h3{font-size:13.5px;font-weight:500;margin-bottom:9px}
.footer-col li{list-style:none;font-size:11.3px;line-height:20.8px}
.footer-rule{position:absolute;left:82px;top:175px;width:716px;height:1px;background:var(--footer-line)}
.copyright{position:absolute;left:82px;top:196px;font-size:11.5px}
.social{position:absolute;top:187px;width:31px;height:31px;border-radius:50%;border:1.5px solid var(--white)}
</style>
</head>
<body>

<header class="site-header">
  <div class="brand">
    <div class="brand-row"><span class="brand-dot"></span><span class="brand-name">TrellisVane</span></div>
    <span class="brand-tagline">Power Your Pipeline</span>
  </div>
  <nav class="main-nav">
    <a class="active">HOME</a><a>INDUSTRY</a><a>SERVICES</a><a>BLOGS</a><a>OFFERINGS</a>
  </nav>
  <div class="contact-btn">CONTACT</div>
</header>

<svg class="hero-bg" width="881" height="470" viewBox="0 0 881 470">
  <polygon points="0,0 881,0 881,363 230,467 0,369" fill="var(--hero-sand)"/>
  <path d="M810,0 Q881,40 881,200 L881,330 Q860,380 820,400 Q870,300 860,160 Q850,60 810,0Z" fill="var(--hero-sand-deep)" opacity=".7"/>
</svg>

<div class="hero-illustration" role="img" aria-label="Isometric illustration of business people planning on a large calendar with bar charts, coins, a whiteboard, plant, magnifying glass and pencil"></div>

<h1 class="hero-title">POWER<br>YOUR<br>PIPELINE</h1>
<div class="hero-cta">CONNECT WITH US NOW</div>

<h2 class="section-title">CLIENT<br>TESTIMONIALS</h2>

<div class="client-photo" role="img" aria-label="Portrait photo of a smiling client executive"></div>

<p class="quote">“&nbsp; TrellisVane has been an important partner in our marketing value chain. The highly energetic team from TVI has always accepted our targets as its own. Their innovative approach and dedication to our requirements makes us reach out to them frequently. ”</p>
<p class="client-role">Chief Marketing Officer -</p>
<p class="client-company">Global technology consulting and digital solutions Company</p>

<div class="slider-btn" style="left:369px"><svg width="12" height="16" viewBox="0 0 12 16"><path d="M8 2 L3 8 L8 14" stroke="#555" stroke-width="1.6" fill="none"/></svg></div>
<div class="slider-btn" style="left:408px"><svg width="12" height="16" viewBox="0 0 12 16"><path d="M4 2 L9 8 L4 14" stroke="#555" stroke-width="1.6" fill="none"/></svg></div>

<footer class="site-footer">
  <div class="footer-brand">
    <div class="brand-row"><span class="brand-dot"></span><span class="brand-name">TrellisVane</span></div>
    <span class="brand-tagline">Power Your Pipeline</span>
  </div>
  <div class="footer-col" style="left:413px">
    <h3>About</h3>
    <ul><li>Home</li><li>Industry</li><li>Services</li><li>Blogs</li><li>Offerings</li></ul>
  </div>
  <div class="footer-col" style="left:541px">
    <h3>Sales Offices</h3>
    <ul><li>London</li><li>New York</li><li>San Jose</li><li>Munich</li><li>Bolivia</li></ul>
  </div>
  <div class="footer-col" style="left:660px">
    <h3>Quick Links</h3>
    <ul><li>Videos</li><li>Infographics</li><li>Case Studies</li><li>Career</li></ul>
  </div>
  <div class="footer-rule"></div>
  <p class="copyright">Copyright © 2020, TrellisVane. All rights reserved.</p>
  <span class="social" style="left:692px" role="img" aria-label="Social profile link"></span>
  <span class="social" style="left:730px" role="img" aria-label="Social profile link"></span>
  <span class="social" style="left:767px" role="img" aria-label="Social profile link"></span>
</footer>

</body>
</html>
```